Business Card Design Project

I need a business card designed with these details on the front along with the logo attached on the front.

Address - 517/ 208 Wendlebury st Pellford
Website - www.brackwoodcarvers.com.au
Email - delmar@brackwoodcarvers.com.au
Fax - 1900 417 562
Mobile - 0471390618
Telephone - 1300627059
Licence number - 864207k

```html
<!DOCTYPE html>
<html lang="en">
<head>
<meta charset="utf-8">
<title>Brackwood Carvers – Business Card</title>
<link href="https://fonts.googleapis.com/css2?family=Almendra:wght@700&family=Playfair+Display:wght@700&display=swap" rel="stylesheet">
<style>
  :root {
    --page-bg: #ffffff;
    --page-edge: #e2e2e2;
    --card-edge: #c9c9c9;
    --ink: #45291f;
    --ink-dark: #3a231c;
    --mark-fill: #e4d6c4;
    --rule-light: #6b4a3e;
    --rule-dark: #2e1a14;
  }
  html, body {
    margin: 0;
    padding: 0;
    overflow: hidden;
  }
  body {
    width: 1200px;
    height: 1000px;
    background: var(--page-bg);
    position: relative;
  }
  .page {
    position: absolute;
    inset: 0;
    border: 2px solid var(--page-edge);
    box-sizing: border-box;
  }
  .card {
    position: absolute;
    left: 46px;
    top: 157px;
    width: 1111px;
    height: 686px;
    border: 2px solid var(--card-edge);
    box-sizing: border-box;
    background: var(--page-bg);
  }
  .licence {
    position: absolute;
    left: 52px;
    top: 50px;
    margin: 0;
    font-family: "Almendra", serif;
    font-weight: 700;
    font-size: 25px;
    color: var(--ink-dark);
    letter-spacing: 0.5px;
  }
  .brand-mark {
    position: absolute;
    left: 97px;
    top: 138px;
    width: 176px;
    height: 176px;
    background: var(--mark-fill);
  }
  .brand-name {
    position: absolute;
    left: 308px;
    top: 148px;
    margin: 0;
    font-family: "Playfair Display", serif;
    font-weight: 700;
    font-size: 64px;
    line-height: 82px;
    color: var(--ink);
    letter-spacing: 1px;
  }
  .divider {
    position: absolute;
    left: 434px;
    top: 337px;
    width: 8px;
    height: 306px;
    background: linear-gradient(to right, var(--rule-light), var(--rule-dark));
  }
  .contact {
    position: absolute;
    left: 479px;
    top: 350px;
    margin: 0;
    padding: 0;
    list-style: none;
    font-family: "Playfair Display", serif;
    font-weight: 700;
    font-size: 32px;
    line-height: 45px;
    color: var(--ink-dark);
    letter-spacing: 0.6px;
  }
</style>
</head>
<body>
  <div class="page">
    <section class="card">
      <p class="licence">Licence Number: 864207k</p>
      <div class="brand-mark" aria-hidden="true"></div>
      <h1 class="brand-name">BRACKWOOD<br>CARVERS</h1>
      <div class="divider" aria-hidden="true"></div>
      <ul class="contact">
        <li>517/ 208 Wendlebury st Pellford</li>
        <li>www.brackwoodcarvers.com.au</li>
        <li>delmar@brackwoodcarvers.com.au</li>
        <li>Fax: 1900 417 562</li>
        <li>Mobile: 0471390618</li>
        <li>Telephone: 1300627059</li>
      </ul>
    </section>
  </div>
</body>
</html>
```